Fernvale Anglican Church Christmas Advertising

We need a postcard design for our upcoming Christmas events in Dec 2013

This is an exciting time of year and we want to give lots people in the local community a chance to celebrate Christmas with us

Key events
Carols in the Park Sat 14th Dec 5.00pm Wexcombe Park, Lowther St, St Marys (opp church)
Christmas Eve Family Service 6.30pm
Christmas Eve Lessons and Carols 8.30pm
Christmas Day Celebration Service 9.30am

We have a church logo to include. Outline of the church with 2 lines, one green and one yellow line.
The advertising should be fun, punchy and bright colours. Possibly use a line such as Christmas Unwrapped...Jesus is the best present. (this is just an idea)

```html
<!DOCTYPE html>
<html lang="en">
<head>
<meta charset="utf-8">
<title>Fernvale Anglican Church – Christmas Postcard</title>
<link rel="stylesheet" href="https://fonts.googleapis.com/css2?family=Comic+Neue:wght@700&family=Open+Sans:wght@400;600;700&display=swap">
<style>
  :root {
    --page-bg: #e6e6e6;
    --card-white: #ffffff;
    --photo-dark: #0d0f0c;
    --photo-green: #3d7a2c;
    --photo-glow: #8fc35a;
    --gold: #e4a41f;
    --swoosh-grey: #b9bcb8;
    --ink: #262626;
    --rule: #8a8a8a;
    --info-box: #dcdcdc;
  }
  * { margin: 0; padding: 0; box-sizing: border-box; }
  html, body { width: 900px; height: 1200px; overflow: hidden; }
  body {
    background: var(--page-bg);
    font-family: "Open Sans", Arial, sans-serif;
    color: var(--ink);
    position: relative;
  }

  /* Front of card */
  .card-front {
    position: absolute;
    left: 135px; top: 82px;
    width: 633px; height: 488px;
    overflow: hidden;
    background: var(--photo-dark);
  }
  .tree-photo {
    position: absolute; inset: 0;
    background:
      radial-gradient(circle at 78% 72%, var(--photo-green) 0%, #1f4a18 28%, transparent 55%),
      radial-gradient(circle at 12% 22%, rgba(143,195,90,.55) 0%, transparent 22%),
      radial-gradient(circle at 30% 10%, rgba(143,195,90,.35) 0%, transparent 16%),
      var(--photo-dark);
  }
  .headline {
    position: absolute;
    left: 30px; top: 44px; width: 270px;
    font-family: "Comic Neue", "Comic Sans MS", cursive;
    font-weight: 700;
    font-size: 48px;
    line-height: 57px;
    color: #ffffff;
    text-align: center;
  }
  .front-band {
    position: absolute; left: 0; bottom: 0;
    width: 633px; height: 488px;
  }
  .front-brand {
    position: absolute;
    right: 40px; top: 396px;
    color: #ffffff;
    font-weight: 400;
    font-size: 26px;
    line-height: 30px;
    text-align: left;
  }

  /* Back of card */
  .card-back {
    position: absolute;
    left: 135px; top: 637px;
    width: 633px; height: 485px;
    background: var(--card-white);
  }
  .back-brand {
    position: absolute;
    left: 27px; top: 34px;
    font-size: 29px;
    line-height: 34px;
    font-weight: 400;
    color: var(--ink);
  }
  .event-list {
    position: absolute;
    left: 27px; top: 140px; width: 280px;
    list-style: none;
  }
  .event { margin-bottom: 13px; }
  .event-title { font-weight: 700; font-size: 17.5px; line-height: 21px; }
  .event-detail { font-size: 17px; line-height: 21px; }
  .event-detail.small { font-size: 12.5px; line-height: 17px; }
  .location-box {
    position: absolute;
    left: 21px; top: 375px;
    width: 276px; height: 87px;
    background: var(--info-box);
    padding: 9px 8px;
    font-size: 13px;
    line-height: 18px;
  }
  .location-box strong { font-weight: 700; }
  .divider {
    position: absolute;
    left: 318px; top: 22px;
    width: 1px; height: 443px;
    background: var(--rule);
  }
  .stamp-box {
    position: absolute;
    left: 514px; top: 35px;
    width: 78px; height: 104px;
    border: 1px solid #555;
  }
  .address-line {
    position: absolute;
    left: 350px; width: 250px; height: 1px;
    background: var(--rule);
  }
</style>
</head>
<body>

  <section class="card-front">
    <div class="tree-photo" role="img" aria-label="Photo of a clear glass angel ornament playing a trumpet hanging in front of a glowing green Christmas tree with bokeh lights"></div>
    <h1 class="headline">Jesus is the Reason for the Christmas Season</h1>
    <svg class="front-band" viewBox="0 0 633 488" aria-hidden="true">
      <path d="M0 478 C 180 420, 380 372, 633 352 L633 358 C 380 378, 180 428, 0 484 Z" fill="var(--swoosh-grey)"/>
      <path d="M0 486 C 180 432, 380 382, 633 362 L633 488 L0 488 Z" fill="var(--gold)"/>
    </svg>
    <div class="front-brand">Fernvale<br>Anglican Church</div>
  </section>

  <section class="card-back">
    <div class="back-brand">Fernvale<br>Anglican Church</div>

    <ul class="event-list">
      <li class="event">
        <div class="event-title">Carols in the Park Sat</div>
        <div class="event-detail small">14th Dec 5.00pm Wexcombe Park, Lowther St,<br>Fernvale (opp church)</div>
      </li>
      <li class="event">
        <div class="event-title">Christmas Eve</div>
        <div class="event-detail">Family Service 6.30pm</div>
      </li>
      <li class="event">
        <div class="event-title">Christmas Eve</div>
        <div class="event-detail">Lessons and Carols 8.30pm</div>
      </li>
      <li class="event">
        <div class="event-title">Christmas Day</div>
        <div class="event-detail">Celebration Service 9.30am</div>
      </li>
    </ul>

    <div class="location-box">
      <strong>Location:</strong><br>
      Fernvale Anglican Church<br>
      Cnr Ashby and Lowther St, Fernvale<br>
      Office: 02 9000 4127
    </div>

    <div class="divider"></div>
    <div class="stamp-box"></div>
    <div class="address-line" style="top:297px"></div>
    <div class="address-line" style="top:335px"></div>
    <div class="address-line" style="top:373px"></div>
    <div class="address-line" style="top:411px"></div>
  </section>

</body>
</html>
```